Check-up reminder postcard

We require a design for a postcard to remind patients to book their dental check up.

Size: standard postcard 100 x 150mm

We are a small family-focussed dental practice. The design should reflect our brand which is warm & sophisticated as well as incorporate the logo colours. For more information please see our website kellowayfamilydental.com.au.

Target Market(s)

Female aged 30 - 45 years old

Industry/Entity Type

Dental

Requirements
Must have
• The front side should have the copy "We've been missing you...".

Back side of postcard should have area for patient name, address, stamp to be placed. The following copy should be used:

"Dear (please leave space for name)

We've been missing you!

We haven't seen you for your regular dental check up. Please call or visit our website to schedule an appointment. Alternatively, we will be in touch over the next couple of weeks.

We look forward to seeing you again soon!

The Kelloway Family Dental team

Phone: 03 9412 7058 Address: 118 Denholm Road, Kelloway VIC 3152 Web: www.kellowayfamilydental.com.au Email: admin@kellowayfamilydental.com.au"

Include the logo on back side of postcard. Please add the tag line under the logo "Creating beautiful smiles everyday" - sans serif font.

- Design file:
All colours must be converted to CMYK.
Bleed 3mm external from trim.
Trims and registration marks are offset 5mm.
All text to be 3mm from trim if possible.
Nice to have
• Maple leaf as in the logo
Slightly cursive font
Less cluttered look
Should not have
• Cartoons
Pictures of teeth, drills, probes, mirrors
Photos of people

```html
<!DOCTYPE html>
<html lang="en">
<head>
<meta charset="utf-8">
<title>Kelloway Family Dental – Check-up Reminder Postcard</title>
<link rel="stylesheet" href="https://fonts.googleapis.com/css2?family=Alex+Brush&family=Open+Sans:wght@400;600&display=swap">
<style>
  :root {
    --paper: #ffffff;
    --teal: #16848f;
    --ink: #111111;
    --grey: #7a7a7a;
    --leaf-lime: #c3d52a;
    --leaf-mint: #5cc497;
    --leaf-teal: #3fb3a6;
    --leaf-gold: #a89a2c;
    --rule: #000000;
  }
  * { box-sizing: border-box; margin: 0; padding: 0; }
  html, body { width: 780px; height: 1200px; overflow: hidden; background: var(--paper); }
  .postcard { position: relative; width: 780px; height: 1200px; background: var(--paper); }

  /* Front */
  .front { position: absolute; left: 0; top: 0; width: 780px; height: 600px; }
  .front__leaf {
    position: absolute; left: 80px; top: 0; width: 620px; height: 445px;
    border-radius: 0 0 48% 48% / 0 0 62% 62%;
    background: radial-gradient(ellipse at 52% 8%, var(--leaf-lime) 0%, var(--leaf-mint) 45%, var(--leaf-teal) 100%);
  }
  .front__headline {
    position: absolute; left: 0; right: 0; top: 488px;
    text-align: center; font-family: "Alex Brush", cursive;
    font-size: 64px; color: var(--teal); line-height: 1;
  }
  .fold { position: absolute; left: 0; top: 600px; width: 780px; height: 1px; background: var(--rule); }

  /* Back – message side */
  .brand {
    position: absolute; left: 45px; top: 652px; width: 360px;
    font-family: "Open Sans", sans-serif; font-weight: 600;
    font-size: 34px; line-height: 1.15; color: var(--teal);
  }
  .message {
    position: absolute; left: 45px; top: 766px; width: 360px;
    font-family: "Open Sans", sans-serif; font-size: 16px; line-height: 20px; color: var(--ink);
  }
  .message p { margin-bottom: 20px; }
  .message p.contact { margin-bottom: 0; }
  .tagline {
    position: absolute; left: 34px; top: 1118px;
    font-family: "Alex Brush", cursive; font-size: 31px; color: var(--teal); line-height: 1;
  }
  .leaf-column {
    position: absolute; left: 431px; top: 630px; width: 44px; height: 550px;
    border-radius: 22px;
    background: linear-gradient(180deg, var(--leaf-gold), var(--leaf-mint) 50%, var(--leaf-gold));
    opacity: 0.75;
  }

  /* Back – address side */
  .stamp-box { position: absolute; left: 643px; top: 627px; width: 111px; height: 128px; border: 2px solid var(--grey); }
  .address-line { position: absolute; left: 511px; width: 240px; height: 3px; background: var(--grey); }
  .address-line--1 { top: 931px; }
  .address-line--2 { top: 968px; }
  .address-line--3 { top: 1006px; }
</style>
</head>
<body>
<main class="postcard">
  <section class="front">
    <div class="front__leaf" role="img" aria-label="Large green maple leaf illustration"></div>
    <h1 class="front__headline">We Have Been Missing You....</h1>
  </section>

  <div class="fold"></div>

  <section class="back">
    <div class="brand">Kelloway<br>Family Dental</div>

    <div class="message">
      <p>Dear,</p>
      <p>We've been missing you as we haven't seen you for your dental check up.</p>
      <p>Please call or visit our website to book an appointment. Otherwise, we'll be in touch over the next couple of weeks to schedule an appointment.</p>
      <p>We look forward to seeing you again soon!</p>
      <p>The Kelloway Family Dental Team</p>
      <p class="contact">Phone: 03.9412.7058<br>www.kellowayfamilydental.com.au</p>
    </div>

    <div class="tagline">Creating Beautiful Smiles Everyday</div>

    <div class="leaf-column" role="img" aria-label="Vertical column of small maple leaf ornaments"></div>

    <div class="stamp-box" aria-label="Stamp area"></div>
    <div class="address-line address-line--1"></div>
    <div class="address-line address-line--2"></div>
    <div class="address-line address-line--3"></div>
  </section>
</main>
</body>
</html>
```